Health & Hygeine product flyer

Looking to make a 1 page brochure of products to do with health & sanitisation. Hand Sanitiser, disinfect wipes, Hand Sanitiser dispensers. We are a cleaning company and looking to add these products to our consumables line, and market to existing client base.
I will require our mock up label to be placed on the Hand Sanitiser bottles, and anti bacterial wipes as part of the design

Requirements
Must have
• sharp, crisp, fresh design

```html
<!DOCTYPE html>
<html lang="en">
<head>
<meta charset="utf-8">
<title>Veltra Corporation – Health &amp; Hygiene Products</title>
<link href="https://fonts.googleapis.com/css2?family=Anton&family=Montserrat:wght@400;500;700;800&display=swap" rel="stylesheet">
<style>
:root{
  --navy:#3d4492;
  --navy-deep:#363c86;
  --blue:#4d7fc2;
  --blue-light:#6f9ad6;
  --ink:#2c2f45;
  --dash:#8e96cc;
  --page:#e4e4e6;
  --white:#ffffff;
}
*{box-sizing:border-box;margin:0;padding:0}
html,body{width:1200px;height:2301px;overflow:hidden;background:var(--page)}
.stage{position:relative;width:1200px;height:2301px}
.flyer{
  position:absolute;left:60px;top:387px;width:775px;height:1095px;
  transform:scale(1.3935);transform-origin:0 0;
  background:var(--white);overflow:hidden;
  font-family:"Montserrat",sans-serif;color:var(--ink);
  box-shadow:0 2px 8px rgba(0,0,0,.12);
}
.header-art{position:absolute;left:0;top:0}
.brand{
  position:absolute;left:53px;top:86px;display:flex;align-items:center;gap:8px;
  font-family:"Montserrat",sans-serif;font-weight:500;font-size:12px;letter-spacing:3px;color:var(--white);
}
.brand-square{width:14px;height:14px;background:var(--white)}
.headline{position:absolute;left:52px;top:176px;font-family:"Anton",sans-serif;color:var(--white);line-height:1;letter-spacing:.5px}
.headline .line-small{display:block;font-size:41px;transform:scaleX(.88);transform-origin:left}
.headline .line-big{display:block;font-size:52px;margin-top:6px;transform:scaleX(.86);transform-origin:left}
.headline-rule{position:absolute;left:53px;top:300px;width:197px;height:6px;background:var(--white)}
.section-title{position:absolute;left:53px;top:389px;font-weight:800;font-size:17px;color:var(--navy);letter-spacing:.2px}
.section-rule{position:absolute;left:53px;top:414px;width:48px;height:4px;background:var(--navy)}
.card{
  position:absolute;width:299px;height:116px;background:var(--white);padding:6px;
  box-shadow:0 2px 5px rgba(40,45,90,.22);
}
.card.wide{width:535px;height:118px}
.card-inner{width:100%;height:100%;border:1px dashed var(--dash);position:relative}
.product-shot{position:absolute;top:12px;bottom:12px;left:10px;width:82px;border-radius:6px}
.card-text{position:absolute;left:129px;top:0;bottom:0;display:flex;flex-direction:column;justify-content:center}
.card.wide .card-text{left:343px}
.product-name{font-weight:700;font-size:12px;line-height:1.2;color:var(--navy);letter-spacing:.4px;text-transform:uppercase}
.product-spec{font-size:10px;line-height:1.5;margin-top:6px}
.product-spec + .product-spec{margin-top:0}
.price{font-weight:700;font-size:11.5px;margin-top:6px}
.price-note{font-size:10px;line-height:1.1}
.footer{position:absolute;left:0;top:1035px;width:775px;height:60px}
.footer-art{position:absolute;left:0;top:0}
.call{position:absolute;left:53px;top:10px;color:var(--white)}
.call-label{font-weight:800;font-size:14px;letter-spacing:.3px}
.call-number{font-weight:500;font-size:21px;letter-spacing:.5px;margin-top:0}
.contact{position:absolute;top:23px;display:flex;align-items:center;gap:9px;color:var(--white);font-size:12.5px;font-weight:500}
.contact.email{left:277px}
.contact.web{left:535px}
</style>
</head>
<body>
<div class="stage">
  <div class="flyer">
    <svg class="header-art" width="775" height="420" viewBox="0 0 775 420" aria-hidden="false">
      <defs>
        <linearGradient id="headerFill" x1="0" y1="0" x2="1" y2="0">
          <stop offset="0" stop-color="#3d4492"/>
          <stop offset=".55" stop-color="#4a5fa8"/>
          <stop offset="1" stop-color="#4f86c6"/>
        </linearGradient>
        <linearGradient id="portraitFill" x1="0" y1="0" x2="0" y2="1">
          <stop offset="0" stop-color="#5b8cca"/>
          <stop offset=".5" stop-color="#4d86c8"/>
          <stop offset="1" stop-color="#3f78bd"/>
        </linearGradient>
      </defs>
      <polygon points="0,0 775,0 775,398 0,333" fill="url(#headerFill)"/>
      <polygon points="475,25 775,25 775,398 475,373" fill="url(#portraitFill)" role="img" aria-label="Portrait of a cleaning professional in blue scrubs, face mask and gloves"/>
      <line x1="0" y1="340" x2="775" y2="405" stroke="#7c9fd8" stroke-width="4"/>
    </svg>

    <div class="brand"><span class="brand-square"></span>VELTRA CORPORATION</div>
    <h1 class="headline"><span class="line-small">WE ARE A</span><span class="line-big">CLEANING COMPANY</span></h1>
    <div class="headline-rule"></div>

    <h2 class="section-title">OUR PRODUCTS</h2>
    <div class="section-rule"></div>

    <div class="card" style="left:53px;top:450px">
      <div class="card-inner">
        <div class="product-shot" role="img" aria-label="Pack of antibacterial wipes" style="background:linear-gradient(135deg,#f1f3f8,#cfd8e6)"></div>
        <div class="card-text"><p class="product-name">Antibacterial<br>Wipes</p></div>
      </div>
    </div>

    <div class="card" style="left:422px;top:450px">
      <div class="card-inner">
        <div class="product-shot" role="img" aria-label="500ml pump bottle of hand sanitiser" style="left:22px;width:60px;background:linear-gradient(180deg,#eef1f6,#cdd6e4)"></div>
        <div class="card-text" style="left:120px">
          <p class="product-name">500ml Hand Sanitiser<br>(Pump Bottle)</p>
          <p class="product-spec">75% Alcohol</p>
          <p class="product-spec">Kills 99.9% of Germs</p>
          <p class="price" style="margin-top:2px">$12.95 + GST</p>
          <p class="price-note">(minimum 24 units)</p>
        </div>
      </div>
    </div>

    <div class="card" style="left:53px;top:595px">
      <div class="card-inner">
        <div class="product-shot" role="img" aria-label="5 litre jerry can of hand sanitiser" style="left:22px;width:64px;background:linear-gradient(180deg,#f2f3f6,#c9d2df)"></div>
        <div class="card-text">
          <p class="product-name">5 Litre Hand<br>Sanitiser</p>
          <p class="product-spec">75% Alcohol</p>
          <p class="product-spec">Kills 99.9% of Germs</p>
          <p class="price">$109 + GST</p>
        </div>
      </div>
    </div>

    <div class="card" style="left:422px;top:595px">
      <div class="card-inner">
        <div class="product-shot" role="img" aria-label="Wall mounted automatic hand sanitiser dispenser" style="left:30px;width:42px;background:linear-gradient(90deg,#eceef2,#d3d7de)"></div>
        <div class="card-text" style="left:118px">
          <p class="product-name">Wall Mounted<br>Automatic Hand<br>Sanitiser</p>
          <p class="price" style="margin-top:10px">$149 + GST</p>
        </div>
      </div>
    </div>

    <div class="card" style="left:53px;top:740px">
      <div class="card-inner">
        <div class="product-shot" role="img" aria-label="Floor stand automatic hand sanitiser unit" style="left:36px;width:26px;background:linear-gradient(180deg,#eef0f4,#d6dae2)"></div>
        <div class="card-text">
          <p class="product-name">Floor Stand Hand<br>Sanitiser Unit –<br>Automatic</p>
          <p class="price" style="margin-top:10px">$399 + GST</p>
        </div>
      </div>
    </div>

    <div class="card" style="left:422px;top:740px">
      <div class="card-inner">
        <div class="product-shot" role="img" aria-label="Stacks of blue disposable face masks" style="left:12px;width:90px;background:linear-gradient(135deg,#a9d4f2,#5fa9e2)"></div>
        <div class="card-text" style="left:118px">
          <p class="product-name">Anti-Dust Face Mask</p>
          <p class="product-spec" style="margin-top:4px">3 Layer Anti Dust</p>
          <p class="price" style="margin-top:2px">$29.95</p>
          <p class="product-spec" style="margin-top:2px">50 Pcs</p>
        </div>
      </div>
    </div>

    <div class="card wide" style="left:120px;top:885px">
      <div class="card-inner">
        <div class="product-shot" role="img" aria-label="Boxes of nitrile gloves in black and white packaging" style="left:16px;width:290px;background:linear-gradient(90deg,#d8dbe2,#eef0f4 50%,#cfd4de)"></div>
        <div class="card-text" style="left:342px">
          <p class="product-name">Nitrite Gloves</p>
          <p class="product-spec" style="margin-top:8px">S/M/L/XL&nbsp;&nbsp;&nbsp;&nbsp;&nbsp;&nbsp;Pk 100</p>
          <p class="price" style="margin-top:6px">$22.95</p>
        </div>
      </div>
    </div>

    <footer class="footer">
      <svg class="footer-art" width="775" height="60" viewBox="0 0 775 60" aria-hidden="true">
        <rect x="0" y="8" width="775" height="52" fill="#4a79bc"/>
        <polygon points="0,0 230,0 255,60 0,60" fill="#3b4190"/>
      </svg>
      <div class="call">
        <p class="call-label">CALL US</p>
        <p class="call-number">123-456-7890</p>
      </div>
      <div class="contact email">
        <svg width="13" height="10" viewBox="0 0 13 10" aria-hidden="true"><rect x="0.5" y="0.5" width="12" height="9" fill="#fff"/><polyline points="0.5,0.5 6.5,5.5 12.5,0.5" fill="none" stroke="#4a79bc" stroke-width="1.2"/></svg>
        <span>info@veltracorp.com.au</span>
      </div>
      <div class="contact web">
        <svg width="13" height="13" viewBox="0 0 13 13" aria-hidden="true"><g fill="none" stroke="#fff" stroke-width="1.1"><circle cx="6.5" cy="6.5" r="5.8"/><ellipse cx="6.5" cy="6.5" rx="2.5" ry="5.8"/><line x1="0.7" y1="6.5" x2="12.3" y2="6.5"/></g></svg>
        <span>veltracorp.com.au</span>
      </div>
    </footer>
  </div>
</div>
</body>
</html>
```